Aviation security consulting company needs a website

We need a website design for Brisk Holloway, and aviation security consulting company. Brisk Holloway (www.briskholloway.example) is an aviation security consulting company that works with government and industry stakeholders in over 60 countries on aviation security strategy, governance, and oversight at the regulatory and operational level.
Brisk Holloway is strongly internationally focused.
The website required should be simple, corporate, serious, and communicate professionalism, reliability and honesty. We are trying to give the company a feeling of being well established.
The attached files include the company logo, along with examples of company web page styles that we like.
The Brisk Holloway website need only be around five pages long (landing page, who we are, our services, our clients, contact), though don't feel limited to only five pages.
The existing website (www.briskholloway.example) was rushed and put together using Wix. We don't love the existing website as it looks too amateur, so don't use it as a template.
There is no requirement for any online sales tools to be included in the site. The site is purely informational, with the option of people making contact via email.

```html
<!DOCTYPE html>
<html lang="en">
<head>
<meta charset="utf-8">
<title>Brisk Holloway — Aviation Security Consulting</title>
<link href="https://fonts.googleapis.com/css2?family=Open+Sans:wght@400;600;700&family=Ubuntu:wght@500;700&display=swap" rel="stylesheet">
<style>
:root{
  --navy:#141c4c;
  --navy-deep:#0e1540;
  --royal:#2b4fc4;
  --royal-light:#4a6ee0;
  --sky:#6c88b8;
  --page:#ffffff;
  --frame:#e9e9e9;
  --grey-band:#eeeeee;
  --text:#3d3d3d;
  --muted:#9a9a9a;
  --rule:#d4d4d4;
  --white:#ffffff;
}
*{box-sizing:border-box;margin:0;padding:0}
html,body{width:1200px;height:3237px;overflow:hidden}
body{background:var(--frame);font-family:"Open Sans",Arial,sans-serif;color:var(--text);position:relative}
.abs{position:absolute}
.page{position:absolute;left:15px;top:0;width:1170px;height:3237px;background:var(--page)}

/* header */
.brand{left:43px;top:43px;width:357px;height:75px;background:var(--navy);display:flex;align-items:center;gap:14px;padding-left:14px}
.brand-mark{width:44px;height:44px;border:3px solid var(--white)}
.brand-name{font-family:"Open Sans",sans-serif;font-weight:700;font-size:30px;color:var(--white);letter-spacing:-.5px}
.topbar{left:583px;top:0;width:602px;height:69px}
.topbar-info{left:650px;top:0;height:69px;width:520px;display:flex;align-items:center;gap:34px;color:var(--white);font-size:15px;font-weight:600}
.topbar-info span{display:flex;align-items:center;gap:8px}
.social{display:flex;gap:5px}
.social i{display:block;width:20px;height:20px;border:2px solid var(--white);border-radius:50%}

/* nav */
.nav{left:15px;top:145px;width:1170px;height:49px;background:var(--navy);display:flex;align-items:center}
.nav a{color:var(--white);text-decoration:none;font-family:"Ubuntu",sans-serif;font-weight:500;font-size:15px;position:absolute;top:0;height:49px;line-height:49px}
.nav a.active{color:#7ea0ff;background:#1e2a66;padding:0 14px;margin-left:-14px}
.search{left:852px;top:153px;width:264px;height:33px;border:1px solid var(--white);color:var(--white);font-size:14px;padding:0 10px;display:flex;align-items:center;justify-content:space-between}

/* hero */
.hero{left:15px;top:194px;width:1170px;height:601px;background:linear-gradient(160deg,#4f6d9e 0%,#2e4678 40%,#1b2b5c 75%,#121c44 100%)}
.hero-text{left:15px;top:648px;width:1170px;text-align:center;color:var(--white);font-size:29px;line-height:36px;text-shadow:0 1px 3px rgba(0,0,0,.5)}
.dots{left:563px;top:768px;display:flex;gap:6px}
.dots i{width:32px;height:5px;background:var(--white);display:block}

/* section headings */
.sec-title{left:15px;width:1170px;text-align:center;font-family:"Ubuntu",sans-serif;font-weight:700;font-size:28px;color:var(--navy)}
.divider{left:250px;width:700px;height:30px}
.divider::before{content:"";position:absolute;left:0;right:0;top:15px;height:1px;background:var(--rule)}
.divider i{position:absolute;left:338px;top:2px;width:26px;height:26px;background:var(--page);border:3px solid var(--navy)}
.dark .divider::before{background:rgba(255,255,255,.35)}
.dark .divider i{border-color:var(--white);background:var(--navy)}

.body-copy{font-size:13.5px;line-height:21px;text-align:center}
.btn{background:var(--navy);color:var(--white);font-weight:600;font-size:15px;text-align:center;border-radius:3px}

/* what we do */
.services{left:15px;top:1170px;width:1170px;height:610px;background:linear-gradient(180deg,#2b3d73 0%,#1f2e62 55%,#18244f 100%)}
.service{color:var(--white);font-size:13.5px;line-height:21px}
.service h3{font-size:15px;font-weight:700;margin-bottom:1px}
.hub{left:529px;top:1388px;width:151px;height:151px;background:var(--white);display:flex;align-items:center;justify-content:center}
.hub i{width:96px;height:96px;background:var(--navy-deep);display:block}

/* projects */
.projects{left:15px;top:1780px;width:1170px;height:648px;background:var(--grey-band)}
.card{top:1873px;width:350px;height:497px;background:var(--white);box-shadow:0 2px 6px rgba(0,0,0,.12)}
.card-photo{height:235px}
.card p{padding:22px 22px 0;font-size:14px;line-height:21px}
.card-foot{position:absolute;left:0;bottom:0;width:350px;height:90px}
.card-foot span{position:absolute;left:0;right:0;bottom:14px;text-align:center;color:var(--white);font-weight:700;font-size:25px}

/* leadership */
.leader{background:var(--white);box-shadow:0 2px 10px rgba(0,0,0,.15)}
.leader .portrait{position:absolute;border-radius:50%;border:4px solid #f1f1f1}
.leader .tag{position:absolute;left:-10px;right:-10px;text-align:center;color:var(--white)}

/* footer */
.footer{left:15px;top:2903px;width:1170px;height:287px;background:var(--navy-deep)}
.foot-brand{left:58px;top:3025px;display:flex;align-items:center;gap:12px}
.foot-brand i{width:50px;height:50px;border:3px solid var(--white);display:block}
.foot-brand span{color:var(--white);font-weight:700;font-size:30px;letter-spacing:-.5px}
.foot-social{left:174px;top:3106px;display:flex;gap:6px}
.foot-social i{width:22px;height:22px;border:2px solid var(--white);border-radius:50%;display:block}
.foot-title{color:var(--white);font-family:"Ubuntu",sans-serif;font-weight:700;font-size:22px}
.contact-line{left:414px;display:flex;gap:14px;color:var(--white);font-size:15px;line-height:22px}
.field{background:#000;color:var(--white);font-size:14px;font-weight:600;padding:8px 12px}
.send{left:932px;top:3088px;width:106px;height:39px;background:#000;border:1px solid var(--white);color:var(--white);font-size:14px;font-weight:600;display:flex;align-items:center;justify-content:center}
.copyright{left:15px;top:3190px;width:1170px;height:47px;background:#e3e3e3;text-align:center;line-height:24px;font-size:12px;color:#555}
</style>
</head>
<body>
<div class="page"></div>

<!-- header -->
<div class="abs brand"><span class="brand-mark"></span><span class="brand-name">Brisk Holloway</span></div>
<svg class="abs topbar" viewBox="0 0 602 69" aria-hidden="true"><polygon points="0,0 602,0 602,69 48,69" fill="#0e1540"/></svg>
<div class="abs topbar-info">
  <span><svg width="18" height="18" viewBox="0 0 24 24"><path d="M6.6 10.8a15 15 0 006.6 6.6l2.2-2.2a1 1 0 011-.25 11.4 11.4 0 003.6.6 1 1 0 011 1V20a1 1 0 01-1 1A17 17 0 013 4a1 1 0 011-1h3.5a1 1 0 011 1 11.4 11.4 0 00.6 3.6 1 1 0 01-.25 1z" fill="#fff"/></svg>1-800-555-0142</span>
  <span><svg width="20" height="16" viewBox="0 0 24 18"><rect x="1" y="1" width="22" height="16" rx="2" fill="none" stroke="#fff" stroke-width="2"/><path d="M1 2l11 8 11-8" fill="none" stroke="#fff" stroke-width="2"/></svg>info@briskholloway.example</span>
  <span class="social"><i></i><i></i><i></i></span>
</div>

<nav class="abs nav">
  <a class="active" href="#" style="left:93px">HOME</a>
  <a href="#" style="left:168px">WHO WE ARE</a>
  <a href="#" style="left:315px">WHAT WE DO</a>
  <a href="#" style="left:464px">PROJECTS</a>
  <a href="#" style="left:585px">LEADERSHIP</a>
  <a href="#" style="left:723px">CONTACT</a>
</nav>
<div class="abs search">Search Website<svg width="18" height="18" viewBox="0 0 24 24"><circle cx="10" cy="10" r="7" fill="none" stroke="#fff" stroke-width="3"/><path d="M15 15l7 7" stroke="#fff" stroke-width="3"/></svg></div>

<!-- hero -->
<div class="abs hero" role="img" aria-label="Photo of a passenger jet flying through clouds beside a glass office tower"></div>
<p class="abs hero-text">Brisk Holloway works with government and industry on aviation security<br>regulatory and operational strategy, governance, and oversight.</p>
<div class="abs dots"><i></i><i></i><i></i></div>

<!-- who we are -->
<h2 class="abs sec-title" style="top:853px">WHO WE ARE</h2>
<div class="abs divider" style="top:898px"><i></i></div>
<p class="abs body-copy" style="left:90px;top:945px;width:1017px">Lorem ipsum dolor sit amet, consectetuer adipiscing elit, sed diam nonummy nibh euismod tincidunt ut laoreet dolore magna aliquam erat volutpat. Ut wisi enim ad minim veniam, quis nostrud exerci tation ullamcorper suscipit lobortis nisl ut aliquip ex ea commodo consequat. Duis autem vel eum iriure dolor in hendrerit in vulputate velit esse molestie consequat, vel illum dolore eu feugiat nulla facilisis at vero eros et accumsan et iusto odio dignissim qui blandit praesent luptatum zzril delenit augue duis dolore te feugait nulla facilisi.</p>
<div class="abs btn" style="left:455px;top:1070px;width:290px;height:38px;line-height:38px">MORE ABOUT BRISK HOLLOWAY</div>

<!-- what we do -->
<div class="abs services" role="img" aria-label="Dark blue tinted photo of an airliner parked at an airport gate"></div>
<div class="dark">
  <h2 class="abs sec-title" style="top:1228px;color:#fff">WHAT WE DO</h2>
  <div class="abs divider" style="top:1275px"><i></i></div>
</div>
<svg class="abs" style="left:15px;top:1170px" width="1170" height="610" aria-hidden="true">
  <g stroke="rgba(255,255,255,.55)" stroke-width="1.5" fill="none">
    <path d="M395 211 L460 211 L514 262"/>
    <path d="M777 211 L735 211 L665 262"/>
    <path d="M395 377 L460 377 L514 340"/>
    <path d="M777 377 L735 377 L665 340"/>
    <path d="M585 369 L585 444"/>
  </g>
  <g fill="#2b4fc4" stroke="#fff" stroke-width="3">
    <circle cx="347" cy="211" r="47"/><circle cx="822" cy="211" r="47"/>
    <circle cx="347" cy="377" r="47"/><circle cx="822" cy="377" r="47"/>
    <circle cx="585" cy="492" r="47"/>
  </g>
  <g fill="none" stroke="#fff" stroke-width="3" stroke-linecap="round" stroke-linejoin="round">
    <!-- regulators: people -->
    <circle cx="347" cy="190" r="7"/><path d="M335 208h24"/><path d="M347 197v11M327 222v-14h40v14"/>
    <circle cx="327" cy="228" r="4"/><circle cx="347" cy="228" r="4"/><circle cx="367" cy="228" r="4"/><path d="M347 208v16"/>
    <!-- airports: tower -->
    <path d="M808 198h28l-4 12h-20z"/><path d="M814 210l-3 28h22l-3-28"/><path d="M822 186v12M816 192h12"/>
    <!-- capacity: shield -->
    <path d="M347 352l22 8v16c0 14-10 22-22 27-12-5-22-13-22-27v-16z"/><path d="M338 384l18-18M338 374l10-10"/>
    <!-- airlines: globe -->
    <circle cx="822" cy="377" r="22"/><ellipse cx="822" cy="377" rx="9" ry="22"/><path d="M800 377h44M804 366h36M804 388h36"/>
    <!-- air cargo: arrow plane -->
    <path d="M560 492h50M600 482l10 10-10 10M575 480l8 12-8 12"/>
  </g>
</svg>
<div class="abs hub"><i></i></div>
<div class="abs service" style="left:75px;top:1326px;width:230px"><h3>Regulators</h3>Strategic guidance, development of regulation, training, mentoring, and developing aviation security compliance tools.</div>
<div class="abs service" style="left:88px;top:1494px;width:220px"><h3>Capacity Development</h3>Implementing economically sustainable solutions to aviation security challenges in the local environment.</div>
<div class="abs service" style="left:904px;top:1326px;width:225px"><h3>Airports</h3>Ensuring security is incorporated into airport design, conducting security assessments and undertaking strategic planning.</div>
<div class="abs service" style="left:904px;top:1494px;width:230px"><h3>Airlines</h3>Developing programs, conducting assessments, and provide strategic guidance, governance and change management.</div>
<div class="abs service" style="left:669px;top:1608px;width:240px"><h3>Air Cargo</h3>Assisting air cargo operators meet aviation security obligations while ensuring facilitation and profitability are maintained.</div>

<!-- projects -->
<div class="abs projects"></div>
<h2 class="abs sec-title" style="top:1838px">PROJECTS</h2>
<div class="abs divider" style="top:1882px"><i style="background:#eee"></i></div>

<article class="abs card" style="left:56px">
  <div class="card-photo" role="img" aria-label="Photo of a jet flying past a glass building under a cloudy sky" style="background:linear-gradient(170deg,#6f8cbc,#2d4373)"></div>
  <p>Lorem ipsum dolor sit amet, consectetuer adipiscing elit, sed diam nonummy nibh euismod tincidunt ut laoreet dolore magna aliquam erat volutpat. Ut wisi enim ad minim veniam, quis exerci tation ullamcorper suscipit lobortis aliquip ex ea commodo consequat.</p>
  <svg class="card-foot" viewBox="0 0 350 90" aria-hidden="true"><polygon points="0,90 0,28 175,0 350,28 350,90" fill="#141c4c"/></svg>
  <div class="card-foot"><span>Project #1</span></div>
</article>
<article class="abs card" style="left:425px">
  <div class="card-photo" role="img" aria-label="Photo of an airliner nose at the gate at dusk" style="background:linear-gradient(180deg,#5a4a5c,#b3552e 55%,#2a2a2e)"></div>
  <p>Lorem ipsum dolor sit amet, consectetuer adipiscing elit, sed diam nonummy nibh euismod tincidunt ut laoreet dolore magna aliquam erat volutpat. Ut wisi enim ad minim veniam, quis exerci tation ullamcorper suscipit lobortis aliquip ex ea commodo consequat.</p>
  <svg class="card-foot" viewBox="0 0 350 90" aria-hidden="true"><polygon points="0,90 0,28 175,0 350,28 350,90" fill="#141c4c"/></svg>
  <div class="card-foot"><span>Project #2</span></div>
</article>
<article class="abs card" style="left:796px">
  <div class="card-photo" role="img" aria-label="Photo of an airliner being serviced on the apron with ground vehicles" style="background:linear-gradient(180deg,#8fb0d4,#c8d2da 50%,#6d7377)"></div>
  <p>Lorem ipsum dolor sit amet, consectetuer adipiscing elit, sed diam nonummy nibh euismod tincidunt ut laoreet dolore magna aliquam erat volutpat. Ut wisi enim ad minim veniam, quis exerci tation ullamcorper suscipit lobortis aliquip ex ea commodo consequat.</p>
  <svg class="card-foot" viewBox="0 0 350 90" aria-hidden="true"><polygon points="0,90 0,28 175,0 350,28 350,90" fill="#141c4c"/></svg>
  <div class="card-foot"><span>Project #3</span></div>
</article>

<!-- leadership -->
<h2 class="abs sec-title" style="top:2487px">LEADERSHIP</h2>
<div class="abs divider" style="top:2532px"><i></i></div>

<div class="abs leader" style="left:80px;top:2600px;width:179px;height:216px">
  <div class="portrait" role="img" aria-label="Portrait photo of team member" style="left:44px;top:36px;width:90px;height:90px;background:#e8dccb"></div>
  <div class="tag" style="top:163px;height:28px;line-height:28px;background:#a7a9ae;font-size:12px">Dana Mercer</div>
</div>
<div class="abs leader" style="left:457px;top:2600px;width:179px;height:216px">
  <div class="portrait" role="img" aria-label="Portrait photo of team member" style="left:44px;top:36px;width:90px;height:90px;background:#dfe1e3"></div>
  <div class="tag" style="top:163px;height:28px;line-height:28px;background:#a7a9ae;font-size:12px">Ruth Keller</div>
</div>
<div class="abs leader" style="left:244px;top:2579px;width:220px;height:265px">
  <div class="portrait" role="img" aria-label="Portrait photo of team member" style="left:48px;top:38px;width:124px;height:124px;background:#c9b7a8;border-color:#e7e7e7"></div>
  <div class="tag" style="top:198px;height:41px;line-height:41px;background:#141c4c;font-size:18px;font-weight:600">Owen Tallis</div>
</div>
<p class="abs" style="left:693px;top:2580px;width:452px;font-size:14px;line-height:21px">Lorem ipsum dolor sit amet, consectetuer adipiscing elit, sed diam nonummy nibh euismod tincidunt ut laoreet dolore magna aliquam erat volutpat. Ut wisi enim ad minim veniam, quis nostrud exerci tation ullamcorper suscipit lobortis nisl ut aliquip ex ea commodo consequat. Duis autem vel eum iriure dolor in hendrerit in vulputa te velit esse molestie consequat.</p>
<div class="abs btn" style="left:816px;top:2745px;width:190px;height:38px;line-height:38px">LEARN MORE</div>

<!-- footer -->
<footer class="abs footer"></footer>
<div class="abs foot-brand"><i></i><span>Brisk Holloway</span></div>
<div class="abs foot-social"><i></i><i></i><i></i></div>

<h3 class="abs foot-title" style="left:414px;top:2944px">CONTACT INFO</h3>
<div class="abs contact-line" style="top:2991px">
  <svg width="16" height="22" viewBox="0 0 16 22"><path d="M8 0a8 8 0 018 8c0 6-8 14-8 14S0 14 0 8a8 8 0 018-8z" fill="#fff"/><circle cx="8" cy="8" r="3" fill="#0e1540"/></svg>
  <span>Brisk Holloway<br>48 Runway Lane<br>Harbor City, CA 90000</span>
</div>
<div class="abs contact-line" style="top:3078px">
  <svg width="20" height="20" viewBox="0 0 24 24"><path d="M6.6 10.8a15 15 0 006.6 6.6l2.2-2.2a1 1 0 011-.25 11.4 11.4 0 003.6.6 1 1 0 011 1V20a1 1 0 01-1 1A17 17 0 013 4a1 1 0 011-1h3.5a1 1 0 011 1 11.4 11.4 0 00.6 3.6 1 1 0 01-.25 1z" fill="#fff"/></svg>
  <span>+1.800.555.0142</span>
</div>
<div class="abs contact-line" style="top:3121px">
  <svg width="20" height="16" viewBox="0 0 24 18"><rect x="1" y="1" width="22" height="16" rx="2" fill="#fff"/><path d="M1 2l11 8 11-8" fill="none" stroke="#0e1540" stroke-width="2"/></svg>
  <span>info@briskholloway.example</span>
</div>

<h3 class="abs foot-title" style="left:714px;top:2944px">SEND US A MESSAGE</h3>
<div class="abs field" style="left:714px;top:2991px;width:210px;height:39px">Name</div>
<div class="abs field" style="left:714px;top:3041px;width:210px;height:36px">Email</div>
<div class="abs field" style="left:714px;top:3088px;width:210px;height:39px">Phone</div>
<div class="abs field" style="left:932px;top:2991px;width:212px;height:86px">Message</div>
<div class="abs send">SEND</div>

<div class="abs copyright">© 2016 BRISK HOLLOWAY. ALL RIGHTS RESERVED.</div>
</body>
</html>
```